Barvo Grand Opening

I need a one sided flyer that advertises my grand opening for our new equipment dealership.

Grand Opening

New and Used Equipment Sales
Equipment Rentals
Residential, Commercial and Industrial Rental Equipment
Construction and Industrial Supply
Custom Metal Fabrication
Mobile Welding Service
Pickup and Delivery Service
24hr. Emergency Dedicated Service

Now Open!

4362 Mellowfen HWY
Easley, SC 29640

(864) 555 - 0143

7:00am-7:00pm Monday - Friday
8:00am-3:00pm Saturday

www.barvogear.example

```html
<!DOCTYPE html>
<html lang="en">
<head>
<meta charset="utf-8">
<title>Barvo Grand Opening Flyer</title>
<link rel="stylesheet" href="https://fonts.googleapis.com/css2?family=Saira:wght@400;500;600;700;800;900&family=Exo+2:wght@500;800;900&display=swap">
<style>
  :root{
    --red:#e8202a;
    --ink:#16181b;
    --white:#ffffff;
    --line:#2a2a2a;
    --body-font:"Saira", sans-serif;
    --display-font:"Exo 2", sans-serif;
  }
  *{box-sizing:border-box;margin:0;padding:0}
  html,body{width:903px;height:1200px;overflow:hidden;background:#fff}
  .flyer{position:relative;width:903px;height:1200px;overflow:hidden;font-family:var(--body-font);color:var(--white);background:var(--white)}
  .hero{position:absolute;left:0;top:0;width:903px;height:822px;
    background:radial-gradient(ellipse at 78% 55%, #3a3524 0%, #24241f 30%, #17181a 65%, #0f1012 100%);}
  .brand{position:absolute;top:68px;left:0;width:100%;text-align:center;
    font-family:var(--body-font);font-weight:800;font-size:66px;letter-spacing:1px;line-height:1}
  .brand-mark{display:inline-block;width:26px;height:26px;background:var(--red);margin-right:14px;vertical-align:6px}
  .headline{position:absolute;left:0;width:100%;text-align:center;line-height:1;color:var(--white)}
  .headline--grand{top:184px;font-family:var(--display-font);font-weight:900;font-size:121px;letter-spacing:1px}
  .headline--opening{top:294px;font-family:var(--body-font);font-weight:500;font-size:137px;letter-spacing:2px}
  .tag{position:absolute;top:470px;left:302px;width:296px;height:62px;background:var(--red);
    transform:skewX(-8deg);display:flex;align-items:center;justify-content:center}
  .tag span{transform:skewX(8deg);font-weight:800;font-size:40px;letter-spacing:.5px}
  .hours{position:absolute;top:550px;left:0;width:100%;text-align:center;font-weight:500;font-size:34px;line-height:50px}
  .hours .sep{color:var(--red);margin:0 6px}
  .address{position:absolute;top:668px;left:0;width:100%;text-align:center;font-size:31px;font-weight:400;letter-spacing:.5px}
  .address svg{vertical-align:-4px;margin-right:10px}
  .divider-band{position:absolute;top:793px;left:0;width:903px;height:29px;background:var(--red)}
  .services{position:absolute;top:868px;left:60px;width:781px;height:205px;border:1.5px solid var(--line);border-radius:14px;color:var(--ink)}
  .services-title{position:absolute;top:-16px;left:50%;transform:translateX(-50%);background:var(--white);padding:0 18px;
    font-weight:700;font-size:23px;letter-spacing:.5px;white-space:nowrap}
  .service-list{position:absolute;top:30px;list-style:none;font-size:20px;line-height:24px}
  .service-list--left{left:28px}
  .service-list--right{left:396px}
  .service-list li{position:relative;padding-left:22px;margin-bottom:8px}
  .service-list li::before{content:"";position:absolute;left:0;top:7px;width:10px;height:10px;border-radius:50%;background:var(--red);box-shadow:0 0 0 1.5px #111}
  .contact-bar{position:absolute;left:0;top:1110px;width:903px;height:90px;background:var(--red);display:flex;align-items:center;justify-content:center}
  .contact{display:flex;align-items:center;font-size:31px}
  .contact svg{margin-right:10px}
  .contact--phone{font-weight:700;padding-right:22px}
  .contact--web{font-weight:400;padding-left:18px;border-left:1.5px solid rgba(0,0,0,.35);height:52px}
  .contact--web b{font-weight:700}
</style>
</head>
<body>
<main class="flyer">
  <section class="hero" role="img" aria-label="Dark photo of an excavator at a construction site at dusk"></section>

  <div class="brand"><span class="brand-mark"></span>Barvo</div>
  <h1 class="headline headline--grand">GRAND</h1>
  <p class="headline headline--opening">OPENING</p>

  <div class="tag"><span>NOW OPEN!</span></div>

  <div class="hours">
    <p>Monday - Friday<span class="sep">|</span>7:00 a.m. - 7:00 p.m.</p>
    <p>Saturday<span class="sep">|</span>8:00 a.m. - 3:00 p.m.</p>
  </div>

  <p class="address">
    <svg width="26" height="26" viewBox="0 0 24 24" aria-hidden="true"><circle cx="12" cy="12" r="12" fill="#e8202a"/><path d="M12 5a4.5 4.5 0 0 0-4.5 4.5c0 3.4 4.5 8.5 4.5 8.5s4.5-5.1 4.5-8.5A4.5 4.5 0 0 0 12 5z" fill="#fff"/><circle cx="12" cy="9.5" r="1.8" fill="#e8202a"/></svg>4362 Mellowfen HWY Easley, SC 29640
  </p>

  <div class="divider-band"></div>

  <section class="services">
    <h2 class="services-title">SERVICES WE OFFER</h2>
    <ul class="service-list service-list--left">
      <li>New and Used Equipment Sales</li>
      <li>Equipment Rentals</li>
      <li>Residential, Commercial and<br>Industrial Rental Equipment</li>
      <li>Custom Metal Fabrication</li>
    </ul>
    <ul class="service-list service-list--right">
      <li>Construction and Industrial Supply</li>
      <li>Mobile Welding Service</li>
      <li>Pickup and Delivery Service</li>
      <li>24 hr. Emergency<br>Dedicated Service</li>
    </ul>
  </section>

  <footer class="contact-bar">
    <div class="contact contact--phone">
      <svg width="28" height="28" viewBox="0 0 24 24" aria-hidden="true"><circle cx="12" cy="12" r="12" fill="#111"/><path d="M8.3 6.2l1.9-.4 1.1 2.7-1.3 1a7 7 0 0 0 3.5 3.5l1-1.3 2.7 1.1-.4 1.9c-4.8.4-8.9-3.7-8.5-8.5z" fill="#fff"/></svg>
      (864) 555 - 0143
    </div>
    <div class="contact contact--web">
      <svg width="28" height="28" viewBox="0 0 24 24" aria-hidden="true"><circle cx="12" cy="12" r="12" fill="#111"/><circle cx="12" cy="12" r="6.5" fill="none" stroke="#fff" stroke-width="1.4"/><ellipse cx="12" cy="12" rx="3" ry="6.5" fill="none" stroke="#fff" stroke-width="1.2"/><path d="M5.5 12h13" stroke="#fff" stroke-width="1.2"/></svg>
      www.<b>barvogear</b>.example
    </div>
  </footer>
</main>
</body>
</html>
```